A bar in Newtown, NSW needs a website

We need a website design for a small speakeasy-style bar in Newtown, NSW Australia. The website needs to be simple to navigate, minimalistic, and feature light colours.

The functionality has to be fairly simple:

Main page (navigates to things below)
Food menu
Beverage menu
Bookings

Social media links and misc info at the bottom of every page.

The menus pages need to have space for text inserted as a jpeg file.

Name and logo are attached.

Coding

Coded - Design and coding required

Number of Pages Required

4 page

```html
<!DOCTYPE html>
<html lang="en">
<head>
<meta charset="utf-8">
<title>The Copper Lantern — Home</title>
<link rel="stylesheet" href="https://fonts.googleapis.com/css2?family=Tinos:ital,wght@0,400;0,700;1,400&display=swap">
<style>
  :root {
    --maroon: #5a1a1f;
    --maroon-glass: rgba(88, 22, 28, 0.86);
    --maroon-card: rgba(84, 16, 22, 0.9);
    --gold: #f2c12e;
    --white: #ffffff;
    --soft-text: #d9c2c2;
    --logo-ink: #141414;
    --photo-warm: #c9a585;
    --photo-light: #e2cbb2;
    --photo-deep: #9c6f52;
  }
  * { box-sizing: border-box; margin: 0; padding: 0; }
  html, body { width: 1200px; height: 668px; overflow: hidden; }
  body { font-family: "Tinos", "Times New Roman", serif; color: var(--white); }

  .page { position: relative; width: 1200px; height: 668px; overflow: hidden; }

  .hero-photo {
    position: absolute; inset: 0;
    background:
      radial-gradient(circle at 28% 35%, var(--photo-light) 0 12%, transparent 30%),
      radial-gradient(circle at 85% 40%, #d88a3a 0 10%, transparent 28%),
      radial-gradient(circle at 60% 60%, var(--photo-deep) 0 8%, transparent 26%),
      linear-gradient(135deg, var(--photo-warm), var(--photo-light) 45%, var(--photo-warm));
  }

  .site-nav {
    position: absolute; left: 0; top: 0; width: 1200px; height: 67px;
    background: var(--maroon-glass);
  }
  .site-nav a {
    position: absolute; top: 24px; font-size: 16px; line-height: 1;
    color: var(--white); text-decoration: none; letter-spacing: 0.2px;
  }
  .site-nav a.is-active { color: var(--gold); }

  .brand-badge {
    position: absolute; left: 471px; top: -94px; width: 258px; height: 260px;
    border-radius: 50%; background: var(--white);
    border: 3px solid var(--maroon);
    display: flex; align-items: flex-end; justify-content: center; padding-bottom: 58px;
  }
  .brand-name {
    font-size: 25px; font-weight: 700; color: var(--logo-ink);
    text-align: center; line-height: 1.05; letter-spacing: 0.5px;
  }

  .tagline {
    position: absolute; left: 342px; top: 240px; width: 502px; height: 58px;
    background: var(--maroon-glass);
    font-size: 40px; font-style: italic; text-align: center; line-height: 58px;
  }

  .feature {
    position: absolute; top: 371px; width: 329px; height: 195px;
    background: var(--maroon-card);
  }
  .feature-frame {
    position: absolute; left: 15px; top: 14px; right: 15px; bottom: 13px;
    border: 1.5px solid var(--gold);
  }
  .feature-title {
    height: 39px; border-bottom: 1.5px solid var(--gold);
    font-size: 27px; text-align: center; line-height: 41px; letter-spacing: 0.3px;
  }
  .feature-text {
    margin: 8px auto 0; width: 240px;
    font-size: 11.5px; line-height: 16px; text-align: center; color: var(--soft-text);
  }
  .feature-flourish {
    position: absolute; left: 6px; right: 6px; bottom: 6px; height: 34px;
    background: linear-gradient(90deg, rgba(242,193,46,0.35), rgba(242,193,46,0.08) 50%, rgba(242,193,46,0.35));
    border-radius: 4px;
  }

  .site-footer {
    position: absolute; left: 0; top: 624px; width: 1200px; height: 44px;
    background: var(--maroon);
  }
  .site-footer .legal {
    position: absolute; left: 80px; top: 16px; font-size: 12px; color: var(--white);
  }
  .social { position: absolute; right: 80px; top: 6px; display: flex; gap: 14px; }
  .social a {
    display: block; width: 31px; height: 31px; border-radius: 50%; background: var(--white);
  }
</style>
</head>
<body>
<main class="page">
  <div class="hero-photo" role="img" aria-label="Overhead photo of a wooden table spread with mezze dishes: hummus, olives, falafel, salads, flatbread and fries"></div>

  <nav class="site-nav">
    <a href="#" class="is-active" style="left:79px">HOME</a>
    <a href="#" style="left:190px">ABOUT US</a>
    <a href="#" style="left:330px">OUR &nbsp;MENU</a>
    <a href="#" style="left:769px">GALLERY</a>
    <a href="#" style="left:907px">BOOKING</a>
    <a href="#" style="left:1045px">CONTACT</a>
  </nav>

  <div class="brand-badge">
    <div class="brand-name">THE<br>COPPER<br>LANTERN</div>
  </div>

  <h1 class="tagline">Good Food...Good Feelings</h1>

  <section class="feature" style="left:81px">
    <div class="feature-frame">
      <h2 class="feature-title">BOOK ONLINE</h2>
      <p class="feature-text">There are many variations of passages of Lorem Ipsum available, but the majority have suffered alteration in some formlook even slightly believable.</p>
      <div class="feature-flourish" role="img" aria-label="Gold scrolling flourish ornament"></div>
    </div>
  </section>

  <section class="feature" style="left:436px">
    <div class="feature-frame">
      <h2 class="feature-title">MENU</h2>
      <p class="feature-text">There are many variations of passages of Lorem Ipsum available, but the majority have suffered alteration in some formlook even slightly believable.</p>
      <div class="feature-flourish" role="img" aria-label="Gold scrolling flourish ornament"></div>
    </div>
  </section>

  <section class="feature" style="left:792px">
    <div class="feature-frame">
      <h2 class="feature-title">SPECIAL OFFERS</h2>
      <p class="feature-text">There are many variations of passages of Lorem Ipsum available, but the majority have suffered alteration in some formlook even slightly believable.</p>
      <div class="feature-flourish" role="img" aria-label="Gold scrolling flourish ornament"></div>
    </div>
  </section>

  <footer class="site-footer">
    <p class="legal">© 2016 www.thecopperlantern.com | Privacy Policy</p>
    <div class="social">
      <a href="#" aria-label="Social link 1"></a>
      <a href="#" aria-label="Social link 2"></a>
      <a href="#" aria-label="Social link 3"></a>
      <a href="#" aria-label="Social link 4"></a>
    </div>
  </footer>
</main>
</body>
</html>
```